Lirra - food stand (booth) design

We need posters for a small food stand situated in the centre of the city directly in front of a high-class shopping mall (see file 2 - the food stand at the square) . We sell cinnamon rolls which we named Lirra. We are looking for a design of the food stand which would lure the customer from the square in front of the mall of a size 30 meters (100 ft) wide. At the same time, it should be elegant, possibly Provence style in pastel colours.

We need the name and description of the product (meaning: Lirra – cinnamon rolls) to be visible from the front and maybe even the sides of the food stand. At the same time, we need to place the menu on some "wings", attached to the sides of the stand from outside. The menu will consist of 8 products (4 different kinds of Lirra rolls and 4 kinds of coffee). If you could visualize the wings, it would be nice.

We also need the design of the packaging of the product (a box similar to a hamburger box and a coffee cup) which might carry the logo (which we do not have), but again that is up to you. If you design the logo, maybe it should be placed on the outside of the food stand (up to you).

See the enclosed photos of the food stand from the front and the sides. The size of the food stand’s plan view is 2.5 x 2 meters (8.2 x 6.56 ft). The design can be either in the size of the current stickers (which would be replaced by yours) or it can cover the whole stand.

Below are sizes of the panels. We notice only the relevant ones
(for example the upper front is irrelevant, because it's always open, thus invisible). First is always x (eg. horizontal) axis. All sizes in centimeters.
A Front
A1 lower 234 x 40 cm
B Left side
B1 upper 174 x 100 cm
B2 lower 184 x 48 cm
C Right side (with the door)
C1 left 100 x 100 cm
C2 right (door) 48 x 184 cm

We are looking forward to your designs!

Thank you,
Team Lirra

```html
<!DOCTYPE html>
<html lang="en">
<head>
<meta charset="utf-8">
<title>Lirra – Cinnamon Rolls stand panels</title>
<link rel="stylesheet" href="https://fonts.googleapis.com/css2?family=Alfa+Slab+One&family=Roboto+Slab:wght@700&family=Yellowtail&display=swap">
<style>
  :root {
    --page: #e9e8e4;
    --panel: #f4f3ef;
    --plank-line: #2b2b2b;
    --purple: #7e63b0;
    --orange: #ec9127;
    --ink: #1e1e1e;
    --lavender-light: #a08fcf;
    --lavender-dark: #5b4a8e;
  }
  html, body {
    margin: 0;
    width: 1200px;
    height: 911px;
    overflow: hidden;
    background: var(--page);
  }
  .stand {
    position: relative;
    width: 1200px;
    height: 911px;
  }
  .panel {
    position: absolute;
    left: 40px;
    width: 1120px;
    background: var(--panel);
    box-shadow: 0 2px 8px rgba(0,0,0,.12);
    overflow: hidden;
  }
  .panel--upper { top: 40px; height: 510px; }
  .panel--lower { top: 578px; height: 226px; }
  .plank-line {
    position: absolute;
    left: 0;
    width: 100%;
    height: 2px;
    background: var(--plank-line);
    opacity: .75;
  }
  .brand {
    position: absolute;
    left: 300px;
    top: 120px;
    display: flex;
    align-items: center;
    gap: 22px;
  }
  .brand__dot {
    width: 70px;
    height: 70px;
    border-radius: 50%;
    background: var(--orange);
  }
  .brand__name {
    font-family: "Roboto Slab", serif;
    font-weight: 700;
    font-size: 150px;
    line-height: 1;
    color: var(--purple);
  }
  .brand__tagline {
    position: absolute;
    right: 320px;
    top: 382px;
    margin: 0;
    font-family: "Roboto Slab", serif;
    font-weight: 700;
    font-size: 29px;
    line-height: 42px;
    letter-spacing: 1px;
    text-align: right;
    color: var(--ink);
  }
  .menu-count {
    position: absolute;
    top: 58px;
    text-align: right;
  }
  .menu-count--rolls { left: 46px; width: 310px; }
  .menu-count--coffee { left: 748px; width: 310px; }
  .menu-count__number {
    display: block;
    font-family: "Alfa Slab One", serif;
    font-size: 72px;
    line-height: 1;
    text-shadow: 4px 4px 0 var(--ink);
  }
  .menu-count--rolls .menu-count__number { color: var(--orange); }
  .menu-count--coffee .menu-count__number { color: var(--purple); }
  .menu-count__label {
    display: block;
    margin-top: -20px;
    margin-right: 10px;
    font-family: "Yellowtail", cursive;
    font-size: 58px;
    line-height: 1;
    color: var(--ink);
    text-shadow: 2px 2px 0 #ffffff;
  }
  .lavender {
    position: absolute;
    left: 394px;
    top: 0;
    width: 325px;
    height: 180px;
    background: radial-gradient(ellipse at 50% 35%, var(--lavender-light), var(--lavender-dark) 55%, rgba(244,243,239,0) 78%);
  }
</style>
</head>
<body>
<main class="stand">
  <section class="panel panel--upper">
    <div class="plank-line" style="top:67px"></div>
    <div class="plank-line" style="top:180px"></div>
    <div class="plank-line" style="top:284px"></div>
    <div class="plank-line" style="top:394px"></div>
    <div class="plank-line" style="top:506px"></div>
    <div class="brand">
      <span class="brand__dot"></span>
      <span class="brand__name">Lirra</span>
    </div>
    <p class="brand__tagline">CINNAMON<br>ROLLS</p>
  </section>

  <section class="panel panel--lower">
    <div class="plank-line" style="top:70px"></div>
    <div class="plank-line" style="top:180px"></div>
    <div class="menu-count menu-count--rolls">
      <span class="menu-count__number">4KINDS</span>
      <span class="menu-count__label">of rolls</span>
    </div>
    <div class="lavender" role="img" aria-label="Photograph of a hanging bunch of dried lavender"></div>
    <div class="menu-count menu-count--coffee">
      <span class="menu-count__number">4KINDS</span>
      <span class="menu-count__label">of coffee</span>
    </div>
  </section>
</main>
</body>
</html>
```